The Harvest Compass

Cutting Through the Noise to What Actually Works.

Nutrition book

Target Market(s)

People looking to be or get healthy and eat right.

```html
<!DOCTYPE html>
<html lang="en">
<head>
<meta charset="utf-8">
<title>The Harvest Compass — Book Cover</title>
<link rel="stylesheet" href="https://fonts.googleapis.com/css2?family=Inter+Tight:ital,wght@0,400;0,500;0,800;1,400&display=swap">
<style>
  :root {
    --bg: #1b1b19;
    --bar: #5e5e56;
    --accent: #e9a12d;
    --title: #f8f8f6;
    --label: #bdb5a0;
    --muted: #5f5e57;
  }
  * { margin: 0; padding: 0; box-sizing: border-box; }
  html, body { width: 811px; height: 1200px; overflow: hidden; background: var(--bg); }
  .cover {
    position: relative;
    width: 811px; height: 1200px;
    background: var(--bg);
    font-family: "Inter Tight", "Helvetica Neue", Arial, sans-serif;
  }
  .kicker {
    position: absolute; top: 102px; left: 0; width: 100%;
    text-align: center; color: var(--accent);
    font-size: 24px; font-weight: 500; letter-spacing: 0.5px;
  }
  .title {
    position: absolute; top: 145px; left: 0; width: 100%;
    text-align: center; color: var(--title);
    font-size: 76px; font-weight: 800; line-height: 86px;
    letter-spacing: 0.5px; text-transform: uppercase;
  }
  .spine-rule {
    position: absolute; left: 37px; top: 332px;
    width: 11px; height: 506px; background: var(--accent);
  }
  .tier {
    position: absolute; left: 65px; height: 70px;
    background: var(--bar);
    display: flex; align-items: center; padding-left: 26px;
    color: var(--label); font-size: 28px; font-weight: 400;
    text-transform: uppercase; letter-spacing: -0.3px;
  }
  .tier--1 { top: 332px; width: 649px; }
  .tier--2 { top: 441px; width: 551px; }
  .tier--3 { top: 550px; width: 470px; }
  .tier--4 { top: 659px; width: 389px; color: #b0a893; }
  .tier--5 { top: 768px; width: 300px; color: #a49c88; }
  .scale-label {
    position: absolute; color: var(--accent);
    font-size: 22px; font-weight: 500; text-transform: uppercase;
  }
  .scale-label--most { left: 669px; top: 356px; }
  .scale-label--least { left: 328px; top: 794px; }
  .divider {
    position: absolute; left: 259px; top: 898px;
    width: 293px; height: 2px; background: var(--accent);
  }
  .subtitle {
    position: absolute; top: 922px; left: 0; width: 100%;
    text-align: center; color: var(--muted);
    font-size: 22px; font-style: italic; line-height: 26px;
  }
  .author {
    position: absolute; top: 1100px; left: 0; width: 100%;
    text-align: center; color: var(--muted);
    font-size: 22px; font-style: italic; text-transform: uppercase;
  }
</style>
</head>
<body>
<main class="cover">
  <p class="kicker">THE</p>
  <h1 class="title">Harvest<br>Compass</h1>

  <div class="spine-rule"></div>
  <div class="tier tier--1">Calories</div>
  <div class="tier tier--2">Macronutrients</div>
  <div class="tier tier--3">Micronutrients</div>
  <div class="tier tier--4">Food Quality</div>
  <div class="tier tier--5">Timing</div>
  <span class="scale-label scale-label--most">Most</span>
  <span class="scale-label scale-label--least">Least</span>

  <div class="divider"></div>
  <p class="subtitle">Cutting Through the Noise<br>to What Actually Works</p>
  <p class="author">Author Name</p>
</main>
</body>
</html>
```